Brickpaving & Landscaping flyers

I AM LOOKING FOR FLYERS TO PROMOTE MY BUSINESS. BUSINESS DETAILS ARE AS FOLLOWS
GUS ORCHID YARDWORKS
Your local tradesman.
Brick Paving, Pool Capping, Limestone Retaining, Natural & Synthetic Turf, Garden Bed Edging, Pool Fence Footings, Soakwells. Most suburbs North of the river

gusbellam71@mailvine.example 0418827346
Free no obligation quotes
Fully insured and all work guaranteed!
You can find examples of my work and heaps of reviews at www.socialhub.example/orchidyardworks
Corwin/Tallora based
Discounts offered for all local work

Target Market(s)

Home owners

Industry/Entity Type

Business

Font styles to use
Serif

Colors
ec1f27
fbed22
add136

Requirements
Must have
• Colour, Some green and yellow to represent grass and sand (basic links to landscaping)
Nice to have
• A brick pattern design
Should not have
• Shouldnt be too busy

```html
<!DOCTYPE html>
<html lang="en">
<head>
<meta charset="utf-8">
<title>Gus Orchid Yardworks – Flyer</title>
<link href="https://fonts.googleapis.com/css2?family=Open+Sans:ital,wght@0,400;0,600;0,700;1,400;1,600;1,700&display=swap" rel="stylesheet">
<style>
  :root {
    --green: #8cc63f;
    --green-dark: #76b02e;
    --yellow: #f5ea1e;
    --maroon: #6a1b17;
    --ink: #1c1c1c;
    --paper: #ffffff;
    --backdrop: #ececec;
    --paving-light: #d3cb9c;
    --paving-mid: #bdb47d;
    --paving-dark: #a49b66;
  }
  * { margin: 0; padding: 0; box-sizing: border-box; }
  html, body { width: 1141px; height: 1200px; overflow: hidden; background: var(--backdrop); }
  body { font-family: "Open Sans", Arial, sans-serif; color: var(--ink); position: relative; }

  .flyer {
    position: absolute; left: 172px; top: 38px;
    width: 796px; height: 1123px;
    background: var(--paper);
    overflow: hidden;
    box-shadow: 0 2px 10px rgba(0,0,0,0.18);
  }
  .flyer-shapes { position: absolute; inset: 0; }

  .brand { position: absolute; left: 80px; top: 52px; display: flex; align-items: center; gap: 14px; }
  .brand-dot { width: 64px; height: 64px; border-radius: 50%; background: var(--green); }
  .brand-name { font-weight: 700; font-size: 27px; color: var(--green-dark); letter-spacing: 0.2px; }

  .promise {
    position: absolute; left: 497px; top: 48px;
    font-style: italic; font-size: 24px; line-height: 32px; color: var(--maroon);
  }

  .badge-text {
    position: absolute; left: 575px; top: 378px; width: 166px;
    text-align: center; font-weight: 700; color: var(--ink);
    font-size: 15px; line-height: 28px;
  }
  .badge-text .pct { font-size: 26px; line-height: 30px; display: block; }

  .intro { position: absolute; left: 38px; top: 586px; }
  .intro-name { font-weight: 700; font-size: 27px; color: var(--green); letter-spacing: 0.3px; }
  .intro-tag { font-style: italic; font-weight: 700; font-size: 24px; color: var(--maroon); margin-top: 2px; }

  .services {
    position: absolute; left: 63px; top: 680px;
    display: grid; grid-template-columns: 323px 330px; row-gap: 9px;
    list-style: none;
  }
  .services li {
    font-size: 24px; line-height: 28px; color: var(--ink);
    display: flex; align-items: center; gap: 17px;
  }
  .services li::before {
    content: ""; width: 14px; height: 14px; flex: none;
    background: var(--green); border-radius: 2px;
  }

  .details {
    position: absolute; left: 0; right: 0; top: 877px;
    text-align: center; font-weight: 700; font-size: 21px; line-height: 28px;
  }
  .details .base { color: var(--maroon); font-size: 20px; }
  .details .link { color: var(--green); }

  .call { position: absolute; left: 48px; top: 1027px; color: var(--paper); }
  .call-lead { font-size: 20px; margin-left: 2px; }
  .call-line { display: flex; align-items: center; gap: 14px; margin-top: 2px; }
  .call-number { font-weight: 700; font-size: 38px; line-height: 44px; }
</style>
</head>
<body>
<main class="flyer">
  <svg class="flyer-shapes" width="796" height="1123" viewBox="0 0 796 1123" aria-hidden="false">
    <defs>
      <linearGradient id="paving" x1="0" y1="0" x2="1" y2="1">
        <stop offset="0" stop-color="var(--paving-light)"/>
        <stop offset="0.55" stop-color="var(--paving-mid)"/>
        <stop offset="1" stop-color="var(--paving-dark)"/>
      </linearGradient>
      <linearGradient id="swoosh" x1="0" y1="0" x2="1" y2="0">
        <stop offset="0" stop-color="#f5ea1e" stop-opacity="0"/>
        <stop offset="1" stop-color="#f5ea1e"/>
      </linearGradient>
    </defs>

    <rect class="paving-photo" x="0" y="0" width="796" height="720" fill="url(#paving)" role="img" aria-label="Photo of a freshly laid sandstone-coloured block paving patio"/>

    <path class="header-band" d="M0 0 H796 V108 C640 150 480 188 340 184 C210 180 95 135 0 95 Z" fill="var(--paper)"/>
    <path class="header-swoosh" d="M330 184 C500 188 660 150 796 106 V128 C660 172 500 194 330 184 Z" fill="url(#swoosh)"/>

    <path class="mid-swoosh" d="M280 510 C480 508 660 540 796 574" fill="none" stroke="var(--yellow)" stroke-width="4"/>
    <path class="mid-band" d="M0 516 C260 500 560 520 796 582 V720 H0 Z" fill="var(--green)"/>
    <path class="body-panel" d="M0 553 C300 542 570 580 796 676 V1123 H0 Z" fill="var(--paper)"/>

    <g class="discount-badge">
      <circle cx="658" cy="438" r="84" fill="var(--yellow)"/>
      <circle cx="658" cy="438" r="76" fill="none" stroke="var(--paper)" stroke-width="3"/>
      <circle cx="658" cy="438" r="71" fill="none" stroke="#e4d81a" stroke-width="1.5"/>
    </g>

    <path class="footer-swoosh" d="M0 1013 C260 1002 560 1040 796 1106" fill="none" stroke="var(--yellow)" stroke-width="5"/>
    <path class="footer-band" d="M0 1025 C250 1014 550 1050 796 1116 V1123 H0 Z" fill="var(--green)"/>
  </svg>

  <div class="brand">
    <span class="brand-dot"></span>
    <span class="brand-name">Gus Orchid Yardworks</span>
  </div>

  <p class="promise">Fully Insured and<br>All Work Guaranteed!</p>

  <p class="badge-text"><span class="pct">%</span>DISCOUNTS<br>OFFERED FOR ALL<br>LOCAL WORK</p>

  <section class="intro">
    <h1 class="intro-name">GUS ORCHID YARDWORKS</h1>
    <p class="intro-tag">Your local tradesman.</p>
  </section>

  <ul class="services">
    <li>Brick Paving</li>
    <li>Garden Bed Edging</li>
    <li>Pool Capping</li>
    <li>Pool Fence Footings</li>
    <li>Limestone Retaining</li>
    <li>Soakwells</li>
    <li>Natural &amp; Synthetic Turf</li>
    <li>Most suburbs North of the river</li>
  </ul>

  <section class="details">
    <p class="base">Corwin/Tallora based</p>
    <p>You can find examples of my work and</p>
    <p>heaps of reviews at <span class="link">www.socialhub.example/orchidyardworks</span></p>
  </section>

  <section class="call">
    <p class="call-lead">Call today for your FREE QUOTE</p>
    <div class="call-line">
      <svg class="phone-icon" width="40" height="40" viewBox="0 0 40 40" aria-hidden="true">
        <circle cx="20" cy="20" r="18" fill="none" stroke="#fff" stroke-width="3"/>
        <path d="M13 11 c2-1 3 0 4 2 l1 3 c0 1-1 2-2 3 c1 3 3 5 6 6 c1-1 2-2 3-2 l3 1 c2 1 3 2 2 4 c-1 2-3 3-5 2 c-6-2-11-7-13-13 c-1-2 0-4 1-6 z" fill="#fff"/>
      </svg>
      <span class="call-number">0418827346</span>
    </div>
  </section>
</main>
</body>
</html>
```